Bref créative
Vantoria Real Estate
A Forward Thinking Real Estate Company
Modern
Luke Tarrel
President
4817 North Bramwick Road
Atlanta, Georgia 61837
Luke@Vantoria.com
www.vantoria.com
Please keep in mind that the business card will be printed with rounded edges on the corners (they will not be pointed edges).
As for the font, I use two different fonts in the logo - HandelGotDBol and Arial. I think we should use Ariel font for the text of the business card.
Finally, I am looking for a business card design that is unique and out of the box. Looking for creativity and truly something unique with a nice combination of the reds and blacks used in the logo. I have uploaded the AI file for the logo.
The back of the business card must contain the logo and slogan.
In addition, the following descriptive words must be included somewhere in a unique format:
Brokerage -
Consulting -
Development -
Investments -
Management
And finally, the back of the business card must also contain the website address of the company -
this is the AI file with the company logo
front of card with new bottom

```html
<!DOCTYPE html>
<html lang="en">
<head>
<meta charset="utf-8">
<title>Vantoria Real Estate – Business Cards</title>
<link href="https://fonts.googleapis.com/css2?family=Arimo:wght@400;700&display=swap" rel="stylesheet">
<style>
  :root {
    --page-bg: #e4e5e7;
    --brand-red: #c8202a;
    --deep-red: #8f1118;
    --ink: #1d1d1f;
    --charcoal: #2b2b2d;
    --grey-text: #5a5a5e;
    --rule: #b9b9bd;
    --white: #ffffff;
  }
  * { margin: 0; padding: 0; box-sizing: border-box; }
  html, body {
    width: 1200px; height: 891px; overflow: hidden;
    background: var(--page-bg);
    font-family: "Arimo", Arial, sans-serif;
  }
  .sheet { position: relative; width: 1200px; height: 891px; }
  .card {
    position: absolute; width: 500px; height: 286px;
    border-radius: 16px; overflow: hidden;
    box-shadow: 0 10px 24px rgba(0,0,0,.22);
  }
  .card--front-black { left: 70px;  top: 135px; }
  .card--back-black  { left: 630px; top: 135px; }
  .card--front-red   { left: 70px;  top: 470px; }
  .card--back-red    { left: 630px; top: 470px; }

  /* Front */
  .front { background: linear-gradient(180deg, #ffffff 0%, #f1f1f2 100%); }
  .front .brand { position: absolute; left: 26px; top: 86px; width: 214px; }
  .brand-line { display: flex; align-items: center; gap: 8px; }
  .brand-square { width: 22px; height: 22px; background: var(--brand-red); flex: none; }
  .brand-name { font-weight: 700; font-size: 33px; color: var(--ink); letter-spacing: .5px; }
  .tagline { margin-top: 6px; font-size: 9px; color: var(--grey-text); letter-spacing: .3px; }
  .front .divider { position: absolute; left: 252px; top: 40px; width: 1px; height: 150px; background: var(--rule); }
  .front--red .divider { background: var(--brand-red); width: 2px; }
  .contact { position: absolute; left: 270px; top: 44px; color: var(--charcoal); }
  .contact .name { font-weight: 700; font-size: 23px; color: var(--ink); }
  .front--red .contact .name { color: var(--brand-red); }
  .contact .title { font-size: 12px; color: var(--grey-text); margin: 2px 0 12px; }
  .contact p { font-size: 11.5px; line-height: 16px; }
  .band { position: absolute; left: 0; bottom: 0; width: 500px; height: 78px; }
  .band svg { display: block; }
  .band .web {
    position: absolute; left: 0; right: 0; bottom: 16px; text-align: center;
    color: var(--white); font-size: 13px; letter-spacing: 5px; font-weight: 700;
  }

  /* Back */
  .back--black { background: radial-gradient(ellipse at 50% 35%, #3a3a3d 0%, #1a1a1b 70%, #0f0f10 100%); }
  .back--red { background: radial-gradient(ellipse at 50% 35%, #d5252f 0%, #b01a22 65%, var(--deep-red) 100%); }
  .back .mark { position: absolute; left: 0; right: 0; top: 62px; display: flex; justify-content: center; align-items: center; gap: 10px; }
  .back .mark .brand-square { width: 26px; height: 26px; border: 2px solid var(--white); }
  .back--red .mark .brand-square { background: var(--deep-red); }
  .back .brand-name { color: var(--white); font-size: 36px; }
  .back .tagline { text-align: center; color: #d8d8da; position: absolute; left: 0; right: 0; top: 110px; font-size: 10px; }
  .services { position: absolute; left: 0; right: 0; top: 150px; color: var(--white); font-size: 12px; text-align: center; line-height: 20px; }
  .services span::before { content: "•"; color: var(--brand-red); margin: 0 5px 0 10px; }
  .back--red .services span::before { color: var(--white); }
  .back .web {
    position: absolute; left: 0; right: 0; bottom: 38px; text-align: center;
    color: var(--white); font-size: 13px; letter-spacing: 5px; font-weight: 700;
  }
</style>
</head>
<body>
<main class="sheet">

  <section class="card front front--black card--front-black">
    <div class="brand">
      <div class="brand-line"><span class="brand-square"></span><span class="brand-name">VANTORIA</span></div>
      <div class="tagline">A Forward Thinking Real Estate Company</div>
    </div>
    <div class="divider"></div>
    <div class="contact">
      <div class="name">Luke Tarrel</div>
      <div class="title">President</div>
      <p>4817 North Bramwick Road</p>
      <p>Atlanta, Georgia 61837</p>
      <p>P: (404) 555-0172</p>
      <p>F: (404) 555-0189</p>
      <p>E: Luke@Vantoria.com</p>
    </div>
    <div class="band">
      <svg width="500" height="78" viewBox="0 0 500 78">
        <polygon points="0,30 500,4 500,78 0,78" fill="#9a9a9e"/>
        <polygon points="0,36 500,12 500,78 0,78" fill="#1d1d1f"/>
      </svg>
      <div class="web">www.vantoria.com</div>
    </div>
  </section>

  <section class="card back back--black card--back-black">
    <div class="mark"><span class="brand-square"></span><span class="brand-name">VANTORIA</span></div>
    <div class="tagline">A Forward Thinking Real Estate Company</div>
    <div class="services">
      <span>Brokerage</span><span>Consulting</span><span>Development</span><br>
      <span>Investments</span><span>Management</span>
    </div>
    <div class="web">www.vantoria.com</div>
  </section>

  <section class="card front front--red card--front-red">
    <div class="brand">
      <div class="brand-line"><span class="brand-square"></span><span class="brand-name">VANTORIA</span></div>
      <div class="tagline">A Forward Thinking Real Estate Company</div>
    </div>
    <div class="divider"></div>
    <div class="contact">
      <div class="name">Luke Tarrel</div>
      <div class="title">President</div>
      <p>4817 North Bramwick Road</p>
      <p>Atlanta, Georgia 61837</p>
      <p>P: (404) 555-0172</p>
      <p>F: (404) 555-0189</p>
      <p>E: Luke@Vantoria.com</p>
    </div>
    <div class="band">
      <svg width="500" height="78" viewBox="0 0 500 78">
        <polygon points="0,30 500,4 500,78 0,78" fill="#8f1118"/>
        <polygon points="0,36 500,12 500,78 0,78" fill="#c8202a"/>
      </svg>
      <div class="web">www.vantoria.com</div>
    </div>
  </section>

  <section class="card back back--red card--back-red">
    <div class="mark"><span class="brand-square"></span><span class="brand-name">VANTORIA</span></div>
    <div class="tagline">A Forward Thinking Real Estate Company</div>
    <div class="services">
      <span>Brokerage</span><span>Consulting</span><span>Development</span><br>
      <span>Investments</span><span>Management</span>
    </div>
    <div class="web">www.vantoria.com</div>
  </section>

</main>
</body>
</html>
```